Show Me Your Best Ideas, Design a Whisky Label

We need a front label only for a whisky bottle. The label is to be used as a mockup for a product idea.
The design needs to be presented as a 3D render on the 'Product Bottle' image supplied. We will print the image of the bottle.

This label is for a Graduation in 2020. Emphasis should be placed on the word Graduation and the date: 2020.

Text:
Graduation
2020
Single Malt Whisky
Southern Cross Officer College

Target Market(s)

20-25 year old

Font styles to use
Serif
Sans Serif
Decorative

Colors

Designer to choose colors to be used in the design.

Requirements
Must have
• 3D render of finished design

```html
<!DOCTYPE html>
<html lang="en">
<head>
<meta charset="utf-8">
<title>Graduation 2020 Single Malt Whiskey Label</title>
<link rel="stylesheet" href="https://fonts.googleapis.com/css2?family=Cinzel:wght@400;600&family=Pinyon+Script&display=swap">
<style>
  :root {
    --page-bg: #ffffff;
    --frame-gold: #e6d88a;
    --label-navy: #022147;
    --text-gold: #f3e38f;
  }
  * { margin: 0; padding: 0; box-sizing: border-box; }
  html, body {
    width: 1200px;
    height: 1000px;
    overflow: hidden;
    background: var(--page-bg);
  }
  .canvas {
    position: relative;
    width: 1200px;
    height: 1000px;
  }
  .label {
    position: absolute;
    left: 430px;
    top: 384px;
    width: 322px;
    height: 325px;
    background: var(--frame-gold);
  }
  .label-panel {
    position: absolute;
    left: 9px;
    top: 8px;
    width: 305px;
    height: 308px;
    background: var(--label-navy);
    color: var(--text-gold);
    text-align: center;
  }
  .college-mark {
    position: absolute;
    left: 0;
    right: 0;
    top: 14px;
    display: flex;
    flex-direction: column;
    align-items: center;
    gap: 12px;
  }
  .college-mark svg { display: block; }
  .college-name {
    font-family: "Cinzel", serif;
    font-weight: 600;
    font-size: 13px;
    line-height: 1.35;
    letter-spacing: 0.06em;
    color: var(--text-gold);
    text-transform: uppercase;
  }
  .title {
    position: absolute;
    left: 0;
    right: 0;
    top: 138px;
    font-family: "Pinyon Script", cursive;
    font-size: 64px;
    line-height: 1;
    letter-spacing: 0.01em;
    color: var(--text-gold);
  }
  .year {
    position: absolute;
    left: 0;
    right: 0;
    top: 214px;
    font-family: "Cinzel", serif;
    font-weight: 400;
    font-size: 36px;
    line-height: 1;
    letter-spacing: 0.02em;
    color: var(--text-gold);
  }
  .spirit-type {
    position: absolute;
    left: 0;
    right: 0;
    top: 268px;
    font-family: "Cinzel", serif;
    font-weight: 600;
    font-size: 12px;
    line-height: 1;
    letter-spacing: 0.12em;
    color: var(--text-gold);
  }
  .spirit-name {
    position: absolute;
    left: 0;
    right: 0;
    top: 288px;
    font-family: "Cinzel", serif;
    font-weight: 600;
    font-size: 15px;
    line-height: 1;
    letter-spacing: 0.1em;
    color: var(--text-gold);
  }
</style>
</head>
<body>
  <main class="canvas">
    <section class="label" aria-label="Whiskey bottle front label">
      <div class="label-panel">
        <div class="college-mark">
          <svg width="44" height="44" viewBox="0 0 44 44" aria-hidden="true">
            <circle cx="22" cy="22" r="20" fill="none" stroke="var(--text-gold)" stroke-width="2"/>
          </svg>
          <p class="college-name">Southern Cross<br>Officer College</p>
        </div>
        <h1 class="title">Graduation</h1>
        <p class="year">2020</p>
        <p class="spirit-type">SINGLE MALT</p>
        <p class="spirit-name">WHISKEY</p>
      </div>
    </section>
  </main>
</body>
</html>
```